Trailer wrap for home remodeling company in Sarasota County Florida

I need a wrap design for an enclosed trailer. I like the idea of adding a picture of a really nice kitchen or bathroom, possibly a before and after.
Matte black background
Must include the below information
Brindle Oak Remodeling
CGC2807391
941-527–8140
www.brindleoakremodeling.example
Bathrooms,Kitchens, Additions, Remodels
Trusted Expertise. Refined Design
Trailer is currently all black
Updates

Designs are not what we are looking for, very busy

Industry/Entity Type

Home Remodeling

Colors
0054AA
0677BA
7BADD7
CADEEF
E8F1F8

Requirements
Must have
• Matte black background

```html
<!DOCTYPE html>
<html lang="en">
<head>
<meta charset="utf-8">
<title>Brindle Oak Remodeling – Trailer Wrap Panels</title>
<link href="https://fonts.googleapis.com/css2?family=Poppins:ital,wght@0,400;0,500;0,600;0,700;0,800;1,700;1,800&display=swap" rel="stylesheet">
<style>
  :root {
    --matte-black: #000000;
    --white: #ffffff;
    --brand-blue: #03aeef;
    --license-grey: #404040;
  }
  * { margin: 0; padding: 0; box-sizing: border-box; }
  html, body {
    width: 1133px;
    height: 1200px;
    overflow: hidden;
    background: var(--matte-black);
  }
  .wrap {
    position: relative;
    width: 1133px;
    height: 1200px;
    background: var(--matte-black);
    display: flex;
    font-family: "Poppins", sans-serif;
    color: var(--white);
  }
  .panel {
    position: relative;
    width: 566.5px;
    height: 100%;
  }
  .panel > * {
    position: absolute;
    left: 50%;
    transform: translateX(-50%);
    white-space: nowrap;
    text-align: center;
  }
  .brand-mark {
    top: 72px;
    width: 104px;
    height: 104px;
    border: 3px solid var(--white);
  }
  .brand-name {
    top: 222px;
    font-weight: 500;
    color: var(--white);
    line-height: 1.2;
  }
  .brand-name .line-main {
    display: block;
    font-size: 34px;
    letter-spacing: 5px;
  }
  .brand-name .line-sub {
    display: block;
    font-size: 17px;
    letter-spacing: 8px;
    margin-top: 6px;
  }
  .tagline {
    top: 318px;
    font-size: 39px;
    font-weight: 400;
    line-height: 38px;
    letter-spacing: -0.3px;
  }
  .tagline em {
    font-style: italic;
    font-weight: 800;
    color: var(--brand-blue);
  }
  .license {
    top: 421px;
    width: 368px;
    height: 48px;
    background: var(--license-grey);
    font-size: 29px;
    font-weight: 600;
    line-height: 48px;
  }
  .services {
    top: 490px;
    list-style: none;
    display: flex;
    flex-direction: column;
    gap: 18.5px;
  }
  .service {
    width: 275px;
    height: 36px;
    background: var(--brand-blue);
    font-size: 33px;
    font-weight: 600;
    line-height: 38px;
  }
  .phone {
    top: 704px;
    font-size: 50px;
    font-weight: 800;
    color: var(--brand-blue);
    letter-spacing: 0.5px;
  }
  .website {
    top: 768px;
    font-size: 19px;
    font-weight: 600;
  }
</style>
</head>
<body>
<main class="wrap">
  <section class="panel panel-left">
    <div class="brand-mark" aria-hidden="true"></div>
    <h1 class="brand-name"><span class="line-main">BRINDLE OAK</span><span class="line-sub">REMODELING</span></h1>
    <p class="tagline">Trusted <em>EXPERTISE</em><br>Refined <em>DESIGN</em></p>
    <p class="license">License # CGC2807391</p>
    <ul class="services">
      <li class="service">Bathrooms</li>
      <li class="service">Kitchens</li>
      <li class="service">Additions</li>
      <li class="service">Remodels</li>
    </ul>
    <p class="phone">941-527–8140</p>
    <p class="website">www.brindleoakremodeling.example</p>
  </section>
  <section class="panel panel-right">
    <div class="brand-mark" aria-hidden="true"></div>
    <h2 class="brand-name"><span class="line-main">BRINDLE OAK</span><span class="line-sub">REMODELING</span></h2>
    <p class="tagline">Trusted <em>EXPERTISE</em><br>Refined <em>DESIGN</em></p>
    <p class="license">License # CGC2807391</p>
    <ul class="services">
      <li class="service">Bathrooms</li>
      <li class="service">Kitchens</li>
      <li class="service">Additions</li>
      <li class="service">Remodels</li>
    </ul>
    <p class="phone">941-527–8140</p>
    <p class="website">www.brindleoakremodeling.example</p>
  </section>
</main>
</body>
</html>
```